interior designer/stylist looking for a letter press business card to reflect the stylish work

Hello Designers,
I need a business card design for an company called Halvard Interior Design. I'm aiming at the high end residential and private client market in London providing sleek simple interiors. I'd like my business card to be tackboard worthy and expensive looking, i want people to pin it and for it to have a sought after look, and want prospective customers to hire me as their interior designer as my card is so beautiful.
I love letter press design. I also like the use of colour/foil on the edge.
Colour combos & general things I like -
Black and White
Navy Blue and Gold
Neutral colours (muted palette of greys whites navys beiges)
White Marble & brass
Morvane (fashion designer)
....also open to other suggestions....
Please dont take the pink in the attached photos too literally. i'd like the card to look more masculine than feminine.
I'd like Halvard on one side in one font, with interior design underneath so one word will make the statement....... unless anyone has any other ideas, open to suggestions.
I'd like a really simple font and for the whole card to look very graphic.
my details -
Petra Quillby
Interior Designer & Stylist
email petra@halvardinteriordesign.co.uk
phone +447813554019
website wwww.halvardinteriordesign.co.uk
GO GO GO!! EXCITED TO SEE THE OUTCOME!!
x L
Target Market(s)
High End Residential and private clients
Industry/Entity Type
Business
Contact Information for Business Card
Halvard Interior Design & Styling
Petra Quillby
phone +447813554019

```html
<!DOCTYPE html>
<html lang="en">
<head>
<meta charset="utf-8">
<title>Halvard Interior Design — Business Card Concepts</title>
<link rel="stylesheet" href="https://fonts.googleapis.com/css2?family=Figtree:wght@400;500&family=Crimson+Pro:wght@400;600&display=swap">
<style>
  :root {
    --paper: #ffffff;
    --ink: #1f1f1f;
    --charcoal: #1e1e1e;
    --jet: #000000;
    --graphite: #262626;
    --mid-grey: #8a8a8a;
    --soft-grey: #a9a9a9;
    --pattern-light: #efefef;
    --brass: #7b6d4e;
  }
  html, body {
    margin: 0;
    padding: 0;
    width: 831px;
    height: 1200px;
    overflow: hidden;
    background: var(--paper);
  }
  .sheet { display: block; width: 831px; height: 1200px; }
  .card-edge { stroke: var(--brass); stroke-width: 1.4; }
  .card-white { fill: var(--paper); }
  .card-charcoal { fill: var(--charcoal); }
  .card-black { fill: var(--jet); }
  .card-pattern-light { fill: var(--pattern-light); }
  .card-pattern-dark { fill: var(--graphite); }

  .sans { font-family: "Figtree", sans-serif; }
  .serif { font-family: "Crimson Pro", serif; }

  .name-mark { font-weight: 500; font-size: 30px; letter-spacing: 1px; }
  .name-mark--serif { font-weight: 600; font-size: 32px; letter-spacing: 1px; }
  .name-mark--ink { fill: var(--ink); }
  .name-mark--grey { fill: var(--mid-grey); }
  .name-mark--silver { fill: var(--soft-grey); }
  .centred { text-anchor: middle; }

  .holder-name { font-weight: 400; letter-spacing: 1px; }
  .holder-name--white { fill: #ffffff; }
  .holder-name--grey { fill: var(--mid-grey); }
  .holder-role { font-weight: 400; letter-spacing: 0.6px; }
  .holder-role--grey { fill: var(--soft-grey); }
  .holder-role--white { fill: #ffffff; }
  .divider { stroke: var(--mid-grey); stroke-width: 1.2; }

  .contact { font-size: 12px; fill: #ffffff; }
  .contact-label { font-size: 11px; fill: var(--mid-grey); }
  .contact--dark { font-size: 14px; fill: var(--ink); }
  .contact--dark .key { font-weight: 600; }
  .web-line { font-size: 11.5px; fill: var(--ink); }
  .contact--serif { font-size: 14px; fill: var(--ink); }
</style>
</head>
<body>
<svg class="sheet" viewBox="0 0 831 1200" xmlns="http://www.w3.org/2000/svg">

  <!-- Front, white -->
  <g class="card card-front-white">
    <rect class="card-white card-edge" x="35" y="9" width="361" height="233" rx="12"/>
    <g class="sans name-mark name-mark--ink centred">
      <text x="215.5" y="120">HALVARD</text>
      <text x="215.5" y="156">INTERIOR DESIGN</text>
    </g>
  </g>

  <!-- Front, charcoal with name -->
  <g class="card card-front-charcoal">
    <rect class="card-charcoal card-edge" x="419" y="9" width="361" height="233" rx="12"/>
    <g class="sans name-mark name-mark--grey">
      <text x="451" y="80">HALVARD</text>
      <text x="451" y="116">INTERIOR DESIGN</text>
    </g>
    <text class="sans holder-name holder-name--white" x="451" y="197" font-size="16" textLength="150" lengthAdjust="spacingAndGlyphs">PETRA QUILLBY</text>
    <text class="sans holder-role holder-role--grey" x="451" y="212" font-size="11" textLength="148" lengthAdjust="spacingAndGlyphs">Interior Designer &amp; Stylist</text>
  </g>

  <!-- Back, black with contact -->
  <g class="card card-back-black">
    <rect class="card-black card-edge" x="39" y="270" width="360" height="233" rx="12"/>
    <text class="sans holder-name holder-name--grey" x="67.5" y="328.5" font-size="24" textLength="220" lengthAdjust="spacingAndGlyphs">PETRA QUILLBY</text>
    <text class="sans holder-role holder-role--white" x="67.5" y="347" font-size="13" textLength="169" lengthAdjust="spacingAndGlyphs">Interior Designer &amp; Stylist</text>
    <line class="divider" x1="67" y1="363" x2="291" y2="363"/>
    <g class="sans">
      <text class="contact-label" x="67.5" y="437">e</text>
      <text class="contact" x="85" y="437">petra@halvardinteriordesign.co.uk</text>
      <text class="contact-label" x="67.5" y="454.6">t</text>
      <text class="contact" x="85" y="454.6">+44 (0)781 355 4019</text>
      <text class="contact-label" x="67.5" y="473">w</text>
      <text class="contact" x="87" y="473">www.halvardinteriordesign.co.uk</text>
    </g>
  </g>

  <!-- Back, light patterned with contact -->
  <g class="card card-back-pattern">
    <rect class="card-pattern-light card-edge" x="423" y="270" width="360" height="233" rx="12" role="img" aria-label="Faint repeating word pattern background"/>
    <g class="sans contact--dark">
      <text x="451" y="437"><tspan class="key">e</tspan> petra@halvardinteriordesign.co.uk</text>
      <text x="451" y="458"><tspan class="key">t</tspan> +44 (0)781 355 4019</text>
      <text x="451" y="480">www.halvardinteriordesign.co.uk</text>
    </g>
  </g>

  <!-- Front, light patterned -->
  <g class="card card-front-pattern-light">
    <rect class="card-pattern-light card-edge" x="26" y="543" width="363" height="233" rx="12" role="img" aria-label="Faint repeating word pattern background"/>
    <g class="sans name-mark name-mark--ink centred">
      <text x="207.5" y="650">HALVARD</text>
      <text x="207.5" y="686">INTERIOR DESIGN</text>
    </g>
    <text class="sans web-line centred" x="207.5" y="731">www.halvardinteriordesign.co.uk</text>
  </g>

  <!-- Front, dark patterned -->
  <g class="card card-front-pattern-dark">
    <rect class="card-pattern-dark card-edge" x="432" y="547" width="361" height="233" rx="12" role="img" aria-label="Dark repeating word pattern background"/>
    <g class="sans name-mark name-mark--silver centred">
      <text x="612.5" y="660">HALVARD</text>
      <text x="612.5" y="696">INTERIOR DESIGN</text>
    </g>
  </g>

  <!-- Front, white serif -->
  <g class="card card-front-serif">
    <rect class="card-white card-edge" x="26" y="925" width="360" height="233" rx="12"/>
    <g class="serif name-mark--serif name-mark--ink centred">
      <text x="206" y="1038">HALVARD</text>
      <text x="206" y="1076">INTERIOR DESIGN</text>
    </g>
  </g>

  <!-- Back, white serif with contact -->
  <g class="card card-back-serif">
    <rect class="card-white card-edge" x="434" y="921" width="353" height="229" rx="12"/>
    <g class="serif contact--serif">
      <text x="460" y="1083">e petra@halvardinteriordesign.co.uk</text>
      <text x="460" y="1105">t +44 (0)781 355 4019</text>
      <text x="460" y="1126">www.halvardinteriordesign.co.uk</text>
    </g>
  </g>

</svg>
</body>
</html>
```